update of B2B website and conversion to single page

The current website needs to be modernized. I want what is commonly called a single page website. It is not actually a single page. See some examples here:
https://www.brivane.example/
https://www.quorel.example/
https://www.tindlewick.example/
Most or all graphics will be replaced.
Please see the attached spreadsheet for a rough draft of the home page layout. Convert the existing website at https://www.zolvinbyte.example/ to a single page website. We will provide the page content. You will provide all of the design, graphics, development, production deployment. etc. The look and feel should be corporate, polished, premium.

```html
<!DOCTYPE html>
<html lang="en">
<head>
<meta charset="utf-8">
<title>Zolvin Byte — B2B Business Contact Management</title>
<link rel="stylesheet" href="https://fonts.googleapis.com/css2?family=Varela+Round&display=swap">
<style>
:root{
  --teal:#4fc0be;
  --teal-deep:#2fa7a4;
  --orange:#f15a29;
  --yellow:#fbad3c;
  --navy:#34407a;
  --ink:#2b2b2b;
  --text:#333;
  --muted:#9a9a9a;
  --white:#fff;
  --topbar:#d3d8d8;
  --soft:#e4e9ea;
}
*{box-sizing:border-box;margin:0;padding:0}
html,body{width:1200px;height:1200px;overflow:hidden;background:var(--white)}
body{font-family:"Varela Round",sans-serif;color:var(--text);position:relative}
.topbar{position:absolute;left:0;top:0;width:1200px;height:10px;background:var(--topbar)}
.site-header{position:absolute;left:0;top:10px;width:1200px;height:96px;background:var(--white)}
.brand{position:absolute;left:92px;top:20px;display:flex;align-items:center;gap:10px}
.brand-mark{width:30px;height:30px;border-radius:50%;background:var(--yellow)}
.brand-name{font-size:34px;color:var(--yellow);line-height:1}
.brand-tag{position:absolute;left:90px;top:62px;font-size:11px;color:#222;white-space:nowrap}
.main-nav{position:absolute;left:686px;top:36px;display:flex;font-size:14px;color:#222}
.main-nav a{color:inherit;text-decoration:none;position:absolute;white-space:nowrap}
.main-nav .active{color:var(--teal)}
.main-nav .active::after{content:"";position:absolute;left:0;right:0;top:22px;height:2px;background:var(--teal)}
.caret{position:absolute;top:8px;width:0;height:0;border-left:3px solid transparent;border-right:3px solid transparent;border-top:4px solid #bbb}
.caret.teal{border-top-color:var(--teal)}
.search{position:absolute;left:1034px;top:46px}

.hero{position:absolute;left:0;top:106px;width:1200px;height:616px;background:var(--teal)}
.hero-art{position:absolute;left:144px;top:78px;width:480px;height:428px;border-radius:12px;background:linear-gradient(160deg,#5ccac7,#3fb1ae)}
.hero-copy{position:absolute;left:698px;top:186px;width:390px;color:var(--white)}
.hero-title{font-size:29px;line-height:31px;font-weight:400}
.hero-title .dark{color:var(--ink)}
.hero-text{margin-top:28px;font-size:14px;line-height:21px}
.hero-actions{position:absolute;left:698px;top:380px;display:flex;align-items:center}
.btn-primary{width:136px;height:44px;border-radius:22px;background:var(--ink);color:var(--white);font-size:12.5px;display:flex;align-items:center;justify-content:center}
.btn-link{margin-left:23px;font-size:14px;color:var(--white)}
.slider-arrow{position:absolute;top:306px;width:24px;height:2px;background:rgba(255,255,255,.5)}

.feature-strip{position:absolute;left:0;top:722px;width:1200px;height:104px;display:flex}
.feature{position:relative;height:104px;overflow:hidden;color:var(--white)}
.feature .num{position:absolute;top:6px;font-size:86px;line-height:1;opacity:.12}
.feature .title{position:absolute;font-size:21px;line-height:24px;white-space:nowrap}
.feature .sub{position:absolute;font-size:11.5px}
.f1{width:198px;background:#f5f6f6;color:#222}
.f1 .num{color:#ccc;opacity:.4}
.f2{width:272px;background:var(--teal)}
.f3{width:272px;background:var(--orange)}
.f4{width:272px;background:var(--yellow)}
.f5{width:186px;background:var(--navy)}
.strip-shadow{position:absolute;left:0;top:826px;width:1200px;height:50px;background:linear-gradient(#e3e6e6,rgba(255,255,255,0))}

.services{position:absolute;left:0;top:0}
.service{position:absolute;width:300px}
.service .icon{position:absolute;left:0;top:0;width:56px;height:56px;border-radius:50%;display:flex;align-items:center;justify-content:center}
.service h3{position:absolute;left:79px;top:6px;font-size:19px;font-weight:400;line-height:22px;color:#222;width:240px}
.service p{position:absolute;left:80px;top:56px;width:220px;font-size:12.5px;line-height:19px;color:var(--muted)}
</style>
</head>
<body>
<div class="topbar"></div>
<header class="site-header">
  <div class="brand"><span class="brand-mark"></span><span class="brand-name">Zolvin Byte</span></div>
  <div class="brand-tag">Enterprise Data Quality Made Easy</div>
  <nav class="main-nav">
    <a class="active" style="left:0">Home</a><span class="caret teal" style="left:52px"></span>
    <a style="left:72px">Services</a><span class="caret" style="left:138px"></span>
    <a style="left:168px">Blog</a>
    <a style="left:236px">Contacts</a><span class="caret" style="left:316px"></span>
  </nav>
  <svg class="search" width="22" height="22" viewBox="0 0 22 22"><circle cx="9" cy="9" r="7.5" fill="none" stroke="#ccc" stroke-width="1.5"/><line x1="14.5" y1="14.5" x2="20" y2="20" stroke="#ccc" stroke-width="1.5"/></svg>
</header>

<section class="hero">
  <div class="slider-arrow" style="left:0"></div>
  <div class="slider-arrow" style="left:1188px;width:12px"></div>
  <div class="hero-art" role="img" aria-label="Line illustration of marketing elements: laptop with chart, megaphone, magnet, gears, chat bubbles and icons"></div>
  <div class="hero-copy">
    <h1 class="hero-title"><span class="dark">B2B</span> Business Contact Management.</h1>
    <p class="hero-text">Ut wisi enim ad minim veniam, quis nostrud exerci tation ullamcorper suscipit lobortis nisl ut aliquip ex ea commodo consequat eleifend option.</p>
  </div>
  <div class="hero-actions">
    <div class="btn-primary">LEARN MORE</div>
    <div class="btn-link">Our Services &rarr;</div>
  </div>
</section>

<section class="feature-strip">
  <div class="feature f1"><span class="num" style="left:64px">01</span><span class="title" style="left:-10px;top:27px">B Business<br>ntacts</span></div>
  <div class="feature f2"><span class="num" style="left:140px">02</span><span class="title" style="left:40px;top:26px">Solid Connection</span><span class="sub" style="left:40px;top:58px">Mirum est notare quam littera.</span></div>
  <div class="feature f3"><span class="num" style="left:140px">03</span><span class="title" style="left:40px;top:27px">Social Media<br>Marketing</span></div>
  <div class="feature f4"><span class="num" style="left:130px">04</span><span class="title" style="left:38px;top:39px">Email Marketing</span></div>
  <div class="feature f5"><span class="num" style="left:134px">0</span><span class="title" style="left:40px;top:27px">Ads and<br>business Plan</span></div>
</section>
<div class="strip-shadow"></div>

<section class="services">
  <div class="service" style="left:118px;top:921px">
    <div class="icon" style="background:var(--soft)"><svg width="30" height="30" viewBox="0 0 30 30"><ellipse cx="15" cy="24" rx="11" ry="4" fill="var(--yellow)"/><path d="M15 25c-5-7-8-10-8-15a8 8 0 0 1 16 0c0 5-3 8-8 15z" fill="#ef4b4b"/><circle cx="15" cy="10" r="3" fill="#fff"/></svg></div>
    <h3>LOCAL SEARCH EFFECTS</h3>
    <p>Lorem ipsum dolor sit amet, consectetuer adipiscing elit, sed diam nonummy nibh euismod.</p>
  </div>
  <div class="service" style="left:438px;top:921px">
    <div class="icon" style="background:#f2c511"><svg width="30" height="30" viewBox="0 0 30 30"><path d="M4 7l7-3 8 3 7-3v19l-7 3-8-3-7 3z" fill="#fff" stroke="#333" stroke-width="1.5"/><line x1="11" y1="4" x2="11" y2="23" stroke="#333" stroke-width="1.5"/><line x1="19" y1="7" x2="19" y2="26" stroke="#333" stroke-width="1.5"/></svg></div>
    <h3>SEARCH ON MAP</h3>
    <p>Claritas est etiam processus dynamicus, qui sequitur mutationem consuetudium lectorum.</p>
  </div>
  <div class="service" style="left:758px;top:921px">
    <div class="icon" style="background:#2ec4a0"><svg width="30" height="30" viewBox="0 0 30 30" fill="none" stroke="#fff" stroke-width="2"><circle cx="15" cy="6" r="3"/><line x1="15" y1="9" x2="15" y2="26"/><line x1="10" y1="13" x2="20" y2="13"/><path d="M5 18c1 5 5 8 10 8s9-3 10-8"/></svg></div>
    <h3>BUSINESS OPORTUNITY</h3>
    <p>Investigationes demonstraverunt lectores legere me lius quod ii legunt saepius notare.</p>
  </div>
  <div class="service" style="left:118px;top:1098px">
    <div class="icon" style="background:#2ec4a0"><svg width="34" height="34" viewBox="0 0 34 34"><circle cx="17" cy="17" r="14" fill="#ef4b4b"/><circle cx="17" cy="17" r="10" fill="#fff"/><circle cx="17" cy="17" r="6" fill="#ef4b4b"/><circle cx="17" cy="17" r="2.5" fill="#fff"/><line x1="17" y1="17" x2="29" y2="5" stroke="#333" stroke-width="1.5"/></svg></div>
    <h3>PAID SERVICES</h3>
    <p>Claritas est etiam processus dynamicus, qui sequitur mutationem consuetudium lectorum.</p>
  </div>
  <div class="service" style="left:438px;top:1098px">
    <div class="icon" style="background:var(--soft)"><svg width="32" height="30" viewBox="0 0 32 30"><path d="M16 18l14-6-14-6-14 6z" fill="#2ec4a0" stroke="#333"/><path d="M2 16l14 6 14-6" fill="none" stroke="#333"/><path d="M16 14l14-6-14-6-14 6z" fill="#f2c511" stroke="#333"/><path d="M2 20l14 6 14-6" fill="none" stroke="#333"/></svg></div>
    <h3>MULTI LEVEL ACCESS</h3>
    <p>Investigationes demonstraverunt lectores legere me lius quod ii legunt saepius notare.</p>
  </div>
  <div class="service" style="left:758px;top:1098px">
    <div class="icon" style="background:#f3f0d8"><svg width="34" height="28" viewBox="0 0 34 28"><rect x="2" y="4" width="26" height="18" fill="#fff" stroke="#333" stroke-width="1.5"/><path d="M2 4l13 10 13-10" fill="none" stroke="#333" stroke-width="1.5"/><path d="M27 26c-4-3-6-5-6-7a3 3 0 0 1 6-1 3 3 0 0 1 6 1c0 2-2 4-6 7z" fill="#ef4b4b"/></svg></div>
    <h3>CONTACT OTHER BUSINESSES</h3>
    <p>Lorem ipsum dolor sit amet, consectetuer adipiscing elit, sed diam nonummy nibh euismod.</p>
  </div>
</section>
</body>
</html>
```